Business Card Design for Event Planning Company

Create a business card for event planning company using our new logo. After I pick the design, I will need files made for 6 employees. Our company provides event design & logistics services as well as venue management. The font should be sans serif and complementary to the logo. I will need to know the name of the font selected for the final design. The phone numbers listed should be separated by "." not "-"

Address for the card
PO Box 318, Washington, DC 20019

Card One
Lorna Pettibone
lpettibone@galavoyant.com
202.481.7730

Card Two
Miriam Okonkwo
mokonkwo@galavoyant.com
202.556.2047

Card Three
Tessa Varnholt
tvarnholt@galavoyant.com
978.620.4471

Card Four
Robin Fess
rfess@galavoyant.com
202.718.3362

Card Five
Ada-Rose Pelletan-Uzor
adarose@galavoyant.com
202.839.1205

Card Six
Beatrix Holloway
Beatrix@galavoyant.com
202.492.6618

Target Market(s)

Corporate/Non-Profit

Industry/Entity Type

Event Planning

Contact Information for Business Card

Address for the card

Card One
Lorna Pettibone
lpettibone@galavoyant.com
202.481.7730

Card Two
Miriam Okonkwo
202.556.2047

Card Three
Tessa Varnholt
978.620.4471

Card Four
Robin Fess
rfess@galavoyant.com
202.718.3362

Card Five
Ada-Rose Pelletan-Uzor
202.839.1205

Card Six
Beatrix Holloway
202.492.6618

Font styles to use
Sans Serif

Colors

Designer to choose colors to be used in the design.

Requirements
Must have
• Two-sided with logo
Should not have
• Extra colors or be too busy

```html
<!DOCTYPE html>
<html lang="en">
<head>
<meta charset="utf-8">
<title>Galavoyant — Business Card, Front and Back</title>
<link rel="stylesheet" href="https://fonts.googleapis.com/css2?family=Open+Sans:wght@300;400;600&display=swap">
<style>
  :root {
    --teal: #5ba5a4;
    --ink: #1d1c1d;
    --paper: #ffffff;
    --stage: #ecebe8;
    --ornament: #e9f3f3;
  }
  * { box-sizing: border-box; margin: 0; padding: 0; }
  html, body {
    width: 1200px; height: 1200px; overflow: hidden;
    background: var(--stage);
    font-family: "Open Sans", sans-serif;
    color: var(--ink);
  }
  .sheet {
    width: 1200px; height: 1200px;
    display: flex; flex-direction: column; align-items: center; justify-content: center;
    gap: 60px;
  }
  .card {
    position: relative;
    width: 840px; height: 480px;
    overflow: hidden;
    box-shadow: 0 6px 20px rgba(0,0,0,.12);
  }

  /* Front */
  .card--front { background: var(--paper); }
  .front__bar {
    position: absolute; top: 0; left: 330px;
    width: 50px; height: 125px; background: var(--ink);
  }
  .front__band {
    position: absolute; left: 0; right: 0; bottom: 0;
    height: 48px; background: var(--ink);
  }
  .front__tab {
    position: absolute; bottom: 0; left: 520px;
    width: 40px; height: 48px; background: var(--teal);
  }
  .wordmark {
    font-weight: 300; color: var(--teal);
    letter-spacing: 1px; line-height: 1;
    display: flex; align-items: center; gap: 14px;
  }
  .wordmark__dot {
    width: 22px; height: 22px; border-radius: 50%; background: var(--teal);
  }
  .front__brand {
    position: absolute; left: 500px; top: 180px;
    font-size: 52px;
  }
  .contact {
    position: absolute; left: 48px; top: 238px;
    list-style: none;
  }
  .contact__row {
    display: flex; align-items: center; gap: 18px;
    height: 38px; font-size: 15px;
  }
  .contact__row--name { font-size: 27px; font-weight: 400; height: 46px; }
  .contact__icon {
    width: 26px; height: 26px; flex: none; border-radius: 50%;
    background: var(--ink);
    display: flex; align-items: center; justify-content: center;
  }

  /* Back */
  .card--back { background: var(--teal); }
  .back__band {
    position: absolute; left: 0; right: 0; top: 165px;
    height: 205px; background: var(--paper);
  }
  .back__ornament {
    position: absolute; background: var(--ornament); opacity: .95;
  }
  .back__ornament--left {
    left: 70px; top: 70px; width: 230px; height: 145px;
    border-radius: 50% 50% 12px 12px;
  }
  .back__ornament--right {
    right: 0; top: 120px; width: 170px; height: 95px;
    border-radius: 60% 0 12px 40%;
  }
  .back__brand {
    position: absolute; left: 0; right: 0; top: 215px;
    display: flex; flex-direction: column; align-items: center;
  }
  .back__brand .wordmark { font-size: 60px; }
  .back__tagline {
    margin-top: 16px; margin-left: 60px;
    font-size: 11px; letter-spacing: 9px; color: var(--ink);
  }
</style>
</head>
<body>
<main class="sheet">

  <section class="card card--front" aria-label="Card front">
    <div class="front__bar"></div>
    <ul class="contact">
      <li class="contact__row contact__row--name">
        <span class="contact__icon">
          <svg width="14" height="14" viewBox="0 0 14 14"><circle cx="7" cy="4.5" r="3" fill="#fff"/><path d="M1.5 13c0-3 2.5-5 5.5-5s5.5 2 5.5 5z" fill="#fff"/></svg>
        </span>
        Lorna Pettibone
      </li>
      <li class="contact__row">
        <span class="contact__icon">
          <svg width="16" height="16" viewBox="0 0 16 16"><circle cx="8" cy="8" r="6" fill="none" stroke="#fff" stroke-width="1.5"/><circle cx="8" cy="8" r="2.5" fill="none" stroke="#fff" stroke-width="1.5"/></svg>
        </span>
        lpettibone@galavoyant.com
      </li>
      <li class="contact__row">
        <span class="contact__icon">
          <svg width="14" height="14" viewBox="0 0 14 14"><path d="M3 1.5l2 .3.8 2.7-1.4 1.2a8 8 0 0 0 3.9 3.9l1.2-1.4 2.7.8.3 2c-.3.9-1.2 1.5-2.2 1.5A10 10 0 0 1 1.5 3.7c0-1 .6-1.9 1.5-2.2z" fill="#fff"/></svg>
        </span>
        202.481.7730
      </li>
      <li class="contact__row">
        <span class="contact__icon">
          <svg width="12" height="14" viewBox="0 0 12 14"><path d="M6 13.5S1 8.5 1 5.5a5 5 0 0 1 10 0c0 3-5 8-5 8z" fill="#fff"/><circle cx="6" cy="5.5" r="1.8" fill="#1d1c1d"/></svg>
        </span>
        PO Box 318, Washington, DC 20019
      </li>
    </ul>
    <div class="front__brand wordmark"><span class="wordmark__dot"></span>galavoyant</div>
    <div class="front__band"></div>
    <div class="front__tab"></div>
  </section>

  <section class="card card--back" aria-label="Card back">
    <div class="back__ornament back__ornament--left" role="img" aria-label="Decorative floral flourish"></div>
    <div class="back__ornament back__ornament--right" role="img" aria-label="Decorative floral flourish"></div>
    <div class="back__band"></div>
    <div class="back__brand">
      <div class="wordmark"><span class="wordmark__dot"></span>galavoyant</div>
      <div class="back__tagline">EVENT PLANNERS</div>
    </div>
  </section>

</main>
</body>
</html>
```